Targeting Bar and Restaurants with apparel - Flyer maybe trifold or front to back

We need to develop a flyer that stresses the importance for branding your logo and image on apparel. We need to show products, logos, how they can display the apparel. How this can be a money maker, for them. I have included a 4 page flyer as an idea. We are thinking it does not need to be more than 2.

Glassware should be included.

Target Market(s)

Bar and Restaurant owners and getting them to purchase apparel from us

Font styles to use
Serif

Colors
0255a3
aaaaaa

Requirements
Must have
• Local
• Graphic Design work in house
• Promotional Pricing - 25% Off your first order
• Call to action - email Dana@brightwear7.com
• #WearYourBrand
• Logo and website www.brightwear7.com or call 585-376-9208
Nice to have
• Information about uniforms shirts for employees
• Maybe a promotion with stickers
• Add Club 87 or Kessling photos to garments

```html
<!DOCTYPE html>
<html lang="en">
<head>
<meta charset="utf-8">
<title>Brightwear — Bar and Restaurant Apparel Flyer</title>
<link href="https://fonts.googleapis.com/css2?family=Montserrat:wght@400;500;600;700;800&family=Oswald:wght@500;600;700&display=swap" rel="stylesheet">
<style>
  :root{
    --navy:#0c3a93;
    --blue:#2f7fd6;
    --bright:#1b6fd0;
    --brand:#0255a3;
    --stripe:#3d45a6;
    --red:#d4252b;
    --ink:#1f2a44;
    --body:#4a4f5c;
    --rule:#aaaaaa;
    --paper:#ffffff;
    --stage-light:#b9b9b9;
    --stage-dark:#8c8c8c;
  }
  *{box-sizing:border-box;margin:0;padding:0}
  html,body{width:1200px;height:1200px;overflow:hidden}
  body{
    background:radial-gradient(ellipse at 50% 55%,var(--stage-light) 0%,var(--stage-dark) 100%);
    font-family:"Montserrat",Arial,sans-serif;
    position:relative;
  }
  .side-label{
    position:absolute;top:178px;width:300px;text-align:center;
    font-weight:800;font-size:42px;letter-spacing:1px;color:var(--paper);
  }
  .side-label.front{left:172px}
  .side-label.back{left:740px}

  .flyer{
    position:absolute;top:243px;width:490px;height:687px;background:var(--paper);
    overflow:hidden;box-shadow:0 4px 10px rgba(0,0,0,.25);
  }
  .flyer.front{left:78px}
  .flyer.back{left:639px}
  .layer{position:absolute;left:0;top:0}
  .abs{position:absolute}

  /* front */
  .brand-mark{left:24px;top:50px;display:flex;align-items:center;gap:8px;
    font-weight:800;font-size:24px;color:var(--navy);letter-spacing:.5px}
  .brand-mark .dot{width:18px;height:18px;border-radius:50%;background:var(--navy)}
  .hero-photo{left:282px;top:27px;width:204px;height:282px;
    background:linear-gradient(180deg,#d9d9d9 0%,#8f8f8f 60%,#2a2a2a 100%);
    clip-path:polygon(18% 0,82% 0,100% 40%,100% 100%,0 100%,0 40%)}
  .headline-panel{left:50px;top:102px;width:176px;height:267px;background:var(--blue)}
  .headline{left:63px;color:var(--paper);line-height:1}
  .headline.big{font-family:"Oswald",Arial,sans-serif;font-weight:600;font-size:38px;letter-spacing:.5px}
  .headline.mid{font-weight:600;font-size:20px;letter-spacing:.8px}
  .headline-rule{left:64px;top:226px;width:58px;height:2px;background:var(--paper)}
  .offer-badge{left:72px;top:308px;width:126px;height:118px}
  .offer-badge .pct{position:absolute;top:28px;width:100%;text-align:center;
    font-family:"Oswald",Arial,sans-serif;font-weight:600;font-size:28px;color:var(--paper)}
  .offer-badge .ribbon{position:absolute;top:70px;left:0;width:100%;height:24px;
    background:var(--red);border-radius:3px;color:var(--paper);text-align:center;
    font-family:"Oswald",Arial,sans-serif;font-weight:600;font-size:14px;line-height:24px;letter-spacing:.3px}
  .section-title{font-weight:800;font-size:18px;letter-spacing:.5px;color:var(--navy)}
  .section-title span{color:var(--bright)}
  .about-title{left:290px;top:346px}
  .about-copy{left:290px;top:371px;width:173px;font-size:7.2px;line-height:9.6px;color:var(--body);text-align:justify}
  .about-rule{left:280px;top:376px;width:2px;height:86px;background:#d5d5d5}
  .weare-title{left:290px;top:482px}
  .weare-rule{left:280px;top:515px;width:2px;height:65px;background:#d5d5d5}
  .weare-item{left:291px;display:flex;align-items:center;gap:10px;font-size:7.5px;font-weight:600;color:var(--ink)}
  .weare-item svg{width:24px;height:24px}
  .hashtag{left:278px;top:590px;font-family:"Oswald",Arial,sans-serif;font-weight:700;font-size:17px;color:var(--navy)}
  .desk-scene{left:16px;top:458px;width:251px;height:207px;
    background:linear-gradient(180deg,#2c2c2c 0 8%,#f1f3f6 8% 70%,#c9ccd1 70% 100%);border-radius:6px 6px 2px 2px}
  .contact-email{left:284px;top:632px;display:flex;align-items:center;gap:5px;font-weight:500;font-size:13px;color:var(--paper)}
  .contact-row{left:286px;top:655px;display:flex;align-items:center;gap:8px;font-weight:600;font-size:7.5px;color:var(--paper)}
  .contact-row span{display:flex;align-items:center;gap:3px}

  /* back */
  .couple-photo{left:0;top:0;width:219px;height:357px;
    background:linear-gradient(160deg,#eeeeee 0%,#c8c8c8 45%,#5a6f8f 85%,#3d4f6e 100%);
    clip-path:polygon(0 0,100% 0,100% 100%,0 78%)}
  .feature{left:238px;width:225px}
  .feature .icon{width:18px;height:18px}
  .feature .bar{width:81px;height:2px;background:var(--stripe);margin:5px 0 6px}
  .feature h3{font-weight:700;font-size:11.5px;color:var(--ink);letter-spacing:.3px}
  .feature p{font-size:7.2px;line-height:9.6px;color:var(--body);margin-top:6px}
  .core-title{left:0;width:100%;top:378px;text-align:center;font-family:"Oswald",Arial,sans-serif;
    font-weight:600;font-size:30px;letter-spacing:-.5px;color:var(--navy);line-height:1}
  .core-title span{color:var(--bright)}
  .core-rule{left:298px;top:413px;width:63px;height:3px;background:var(--bright)}
  .service{width:149px}
  .service .thumb{position:absolute;left:52px;width:46px;height:46px;border-radius:50%}
  .service .box{position:absolute;left:0;width:149px;height:53px;border:1px solid #cfcfcf;border-top:none;padding:13px 11px 0}
  .service h4{position:absolute;left:0;width:149px;text-align:center;font-weight:700;font-size:11px;color:var(--stripe);letter-spacing:.3px;
    display:flex;align-items:center;gap:6px}
  .service h4::before,.service h4::after{content:"";flex:1;height:1px;background:#cfcfcf}
  .service p{font-size:7.2px;line-height:9.6px;color:var(--body);text-align:justify}
  .back-email{left:44px;top:662px;display:flex;align-items:center;gap:7px;font-weight:500;font-size:14px;color:var(--paper)}
  .back-row{left:300px;top:669px;display:flex;gap:8px;font-weight:600;font-size:7.5px;color:var(--paper)}
  .back-row span{display:flex;align-items:center;gap:3px}
</style>
</head>
<body>

<div class="side-label front">FRONT</div>
<div class="side-label back">BACK</div>

<!-- FRONT SIDE -->
<section class="flyer front">
  <svg class="layer" width="490" height="687" viewBox="0 0 490 687" aria-hidden="true">
    <polygon points="0,142 490,72 490,284 0,368" fill="var(--navy)"/>
    <polygon points="0,570 230,618 264,621 144,687 0,687" fill="var(--navy)"/>
    <polygon points="264,621 490,621 490,687 144,687" fill="var(--blue)"/>
    <polygon points="285,95 460,58 460,68 285,105" fill="var(--stripe)"/>
    <polygon points="246,307 490,270 490,282 246,319" fill="var(--stripe)"/>
  </svg>

  <div class="abs brand-mark"><span class="dot"></span>BRIGHTWEAR</div>

  <div class="abs hero-photo" role="img" aria-label="Photo of a bartender wearing a branded grey zip hoodie over a black staff tee"></div>

  <div class="abs headline-panel"></div>
  <div class="abs headline big" style="top:158px">BRANDED</div>
  <div class="abs headline mid" style="top:200px">PRODUCTS</div>
  <div class="abs headline-rule"></div>
  <div class="abs headline mid" style="top:236px">GUESTS LOVE</div>
  <div class="abs headline big" style="top:259px">TO WEAR</div>

  <div class="abs offer-badge">
    <svg width="126" height="118" viewBox="0 0 126 118" aria-hidden="true">
      <circle cx="63" cy="57" r="56" fill="var(--red)"/>
      <circle cx="63" cy="57" r="45" fill="none" stroke="#fff" stroke-width="1.5"/>
    </svg>
    <div class="pct">25%</div>
    <div class="ribbon">YOUR FIRST ORDER</div>
  </div>

  <div class="abs about-rule"></div>
  <h2 class="abs section-title about-title">ABOUT <span>US</span></h2>
  <p class="abs about-copy">It's been our pleasure to bring bars, restaurants, pubs and breweries the best in custom apparel, glassware and promotional items since 1990. We help you turn your logo into a money maker: staff uniforms, retail tees to sell at the bar, printed pint glasses and stickers your guests take home. We offer screen printing, embroidery, heat press and graphic design. Get your quote today. Serving Marlow Falls and beyond.</p>

  <h2 class="abs section-title weare-title">WE <span>ARE</span></h2>
  <div class="abs weare-rule"></div>
  <div class="abs weare-item" style="top:514px">
    <svg viewBox="0 0 24 24" fill="none" stroke="var(--stripe)" stroke-width="1.2" aria-hidden="true">
      <circle cx="12" cy="11" r="6"/><path d="M6 11h12M12 5c-3 3-3 9 0 12M12 5c3 3 3 9 0 12"/>
      <path d="M2 6V2h4M22 6V2h-4M2 18v4h4M22 18v4h-4"/>
    </svg>
    Local
  </div>
  <div class="abs weare-item" style="top:555px">
    <svg viewBox="0 0 24 24" fill="none" stroke="var(--stripe)" stroke-width="1.2" aria-hidden="true">
      <rect x="2" y="2" width="20" height="20"/><rect x="7" y="6" width="10" height="12"/><path d="M9 10h6M9 13h6"/>
    </svg>
    Graphic Design work in house
  </div>

  <div class="abs hashtag">#WEARYOURBRAND</div>

  <div class="abs desk-scene" role="img" aria-label="Desktop computer showing a restaurant logo being placed on a T-shirt and pint glass in a design program"></div>

  <div class="abs contact-email">
    <svg width="11" height="11" viewBox="0 0 12 12" aria-hidden="true"><circle cx="6" cy="6" r="5.5" fill="#fff"/><path d="M3 4.5h6v3.5H3zM3 4.5l3 2 3-2" fill="none" stroke="var(--blue)" stroke-width="1"/></svg>
    Dana@brightwear7.com
  </div>
  <div class="abs contact-row">
    <span><svg width="7" height="7" viewBox="0 0 10 10" aria-hidden="true"><path d="M2 1l2 2-1 1.5c.8 1.5 1.8 2.5 3 3L7.5 6l2 2-1.5 1.5C4.5 9 1 5.5.5 2.5z" fill="#fff"/></svg>585-376-9208</span>
    <span><svg width="7" height="7" viewBox="0 0 10 10" aria-hidden="true"><circle cx="5" cy="5" r="4.5" fill="#fff"/></svg>www.brightwear7.com</span>
  </div>
</section>

<!-- BACK SIDE -->
<section class="flyer back">
  <div class="abs couple-photo" role="img" aria-label="Photo of two restaurant staff in matching branded grey hoodies and jeans"></div>
  <svg class="layer" width="490" height="687" viewBox="0 0 490 687" aria-hidden="true">
    <polygon points="22,0 219,0 219,165" fill="var(--bright)"/>
    <polygon points="0,294 147,354 147,362 0,306" fill="var(--stripe)"/>
    <polygon points="0,659 490,659 490,687 0,687" fill="var(--blue)"/>
    <polygon points="289,659 490,659 490,668 485,668 485,687 300,687 292,668" fill="var(--navy)"/>
  </svg>

  <div class="abs feature" style="top:16px">
    <svg class="icon" viewBox="0 0 20 20" fill="none" stroke="var(--bright)" stroke-width="1.8" aria-hidden="true"><circle cx="10" cy="10" r="8"/><path d="M10 5v5h-3"/></svg>
    <div class="bar"></div>
    <h3>QUALITY SERVICE</h3>
    <p>We take pride in serving bars and restaurants with a superior level of service, from first sketch to final delivery.</p>
  </div>
  <div class="abs feature" style="top:95px">
    <svg class="icon" viewBox="0 0 20 20" aria-hidden="true"><path d="M3 2v17" stroke="var(--bright)" stroke-width="1.8"/><path d="M4 3c4-2 7 2 13 0v9c-6 2-9-2-13 0z" fill="var(--bright)"/></svg>
    <div class="bar"></div>
    <h3>INDUSTRY KNOWLEDGE</h3>
    <p>We know hospitality. Branded shirts, hats and glassware turn your regulars into walking ads and extra profit at the bar.</p>
  </div>
  <div class="abs feature" style="top:190px">
    <svg class="icon" viewBox="0 0 20 20" aria-hidden="true"><rect x="2" y="7" width="16" height="4" fill="var(--bright)"/><rect x="3" y="12" width="14" height="7" fill="var(--bright)"/><path d="M10 7v12" stroke="#fff" stroke-width="1.5"/><path d="M10 7C8 3 5 3 6 6M10 7c2-4 5-4 4-1" fill="none" stroke="var(--bright)" stroke-width="1.5"/></svg>
    <div class="bar"></div>
    <h3>UNMATCHED EXPERTISE</h3>
    <p>With over 10 years of printing experience and a skilled team, we keep your staff uniforms looking sharp every shift.</p>
  </div>
  <div class="abs feature" style="top:279px">
    <svg class="icon" viewBox="0 0 20 20" fill="none" stroke="var(--bright)" stroke-width="1.5" aria-hidden="true"><path d="M10 2l2.4 5 5.4.6-4 3.7 1.1 5.4L10 14l-4.9 2.7 1.1-5.4-4-3.7 5.4-.6z"/></svg>
    <div class="bar"></div>
    <h3>TOP-NOTCH PRINTING</h3>
    <p>From pint glasses to polos, our machinery delivers crisp, lasting prints that hold up in busy kitchens and bars.</p>
  </div>

  <h2 class="abs core-title"><span>CORE</span> PRINTING SERVICES</h2>
  <div class="abs core-rule"></div>

  <div class="abs service" style="left:10px;top:420px">
    <div class="thumb" style="top:0;background:linear-gradient(160deg,#f3f3f3,#1f4a2e)" role="img" aria-label="Close-up of a screen printed staff tee"></div>
    <h4 style="top:52px">SCREENPRINTING</h4>
    <div class="box" style="top:58px"><p>A popular choice for bulk orders such as staff tees, retail shirts to sell at the bar, and event nights.</p></div>
  </div>
  <div class="abs service" style="left:170px;top:420px">
    <div class="thumb" style="top:0;background:linear-gradient(160deg,#e8413e,#8e1614)" role="img" aria-label="Close-up of red embroidery stitching on an apron"></div>
    <h4 style="top:52px">EMBROIDERY</h4>
    <div class="box" style="top:58px"><p>Great option for server polos, aprons and hats where a classic, professional look is the garment of choice.</p></div>
  </div>
  <div class="abs service" style="left:329px;top:420px">
    <div class="thumb" style="top:0;background:linear-gradient(160deg,#555,#111)" role="img" aria-label="Close-up of tackle twill lettering on a black jersey"></div>
    <h4 style="top:52px">TACKLE TWILL</h4>
    <div class="box" style="top:58px"><p>Perfect for names, numbers or league lettering on your bar's softball and darts team apparel.</p></div>
  </div>

  <div class="abs service" style="left:10px;top:538px">
    <div class="thumb" style="top:0;background:linear-gradient(160deg,#f0e7e0,#c2452a)" role="img" aria-label="Close-up of a heat pressed multi-colour graphic"></div>
    <h4 style="top:54px">HEAT PRESS</h4>
    <div class="box" style="top:60px"><p>Works well for multi-colored artwork or graphics placed on select areas of uniforms and merch.</p></div>
  </div>
  <div class="abs service" style="left:170px;top:538px">
    <div class="thumb" style="top:0;background:linear-gradient(180deg,#f2efe9,#d9a441 60%,#7a4e12)" role="img" aria-label="Branded pint glass filled with beer"></div>
    <h4 style="top:54px">GLASSWARE</h4>
    <div class="box" style="top:60px"><p>Put your logo on pint glasses, mugs and shot glasses your guests will take home and remember.</p></div>
  </div>
  <div class="abs service" style="left:329px;top:538px">
    <div class="thumb" style="top:0;background:linear-gradient(160deg,#6f7fd0,#2b2f7a)" role="img" aria-label="Printed banner and die-cut stickers in purple and blue"></div>
    <h4 style="top:54px">BANNERS</h4>
    <div class="box" style="top:60px"><p>Stand out with banners and die-cut stickers for your patio, windows, menus and events.</p></div>
  </div>

  <div class="abs back-email">
    <svg width="13" height="13" viewBox="0 0 12 12" aria-hidden="true"><circle cx="6" cy="6" r="5.5" fill="#fff"/><path d="M3 4.5h6v3.5H3zM3 4.5l3 2 3-2" fill="none" stroke="var(--blue)" stroke-width="1"/></svg>
    Dana@brightwear7.com
  </div>
  <div class="abs back-row">
    <span><svg width="7" height="7" viewBox="0 0 10 10" aria-hidden="true"><path d="M2 1l2 2-1 1.5c.8 1.5 1.8 2.5 3 3L7.5 6l2 2-1.5 1.5C4.5 9 1 5.5.5 2.5z" fill="#fff"/></svg>585-376-9208</span>
    <span><svg width="7" height="7" viewBox="0 0 10 10" aria-hidden="true"><circle cx="5" cy="5" r="4.5" fill="#fff"/></svg>www.brightwear7.com</span>
  </div>
</section>

</body>
</html>
```